Business Card for TLK Field Services

Would like a large logo on one side. On the other side, logo on one side and company phone number, address, and email on the other side. I don't have a logo so please create one for us.
Updates
I don't have a logo, so please create one for us.
Target Market(s)
Land Surveying
Industry/Entity Type
Surveyor
Contact Information for Business Card
Would like a large logo on one side. On the other side, logo on one side and company phone number, address, and email on the other side
Requirements
Nice to have
- would like the initials to be incorporated with the logo

```html
<!DOCTYPE html>
<html lang="en">
<head>
<meta charset="utf-8">
<title>TLK Field Services – Business Card</title>
<link rel="stylesheet" href="https://fonts.googleapis.com/css2?family=Open+Sans:wght@400;600;700&display=swap">
<style>
  :root {
    --backdrop: #4a423d;
    --card: #0c0c0c;
    --card-edge: #1c1c1c;
    --brand-green: #9cb83c;
    --silver: #cfcfcf;
    --ink-light: #e6e6e6;
    --divider: #2e2e2e;
  }
  * { box-sizing: border-box; margin: 0; padding: 0; }
  html, body {
    width: 1200px; height: 900px; overflow: hidden;
    background: var(--backdrop);
    font-family: "Open Sans", Arial, sans-serif;
  }
  .stage {
    position: relative; width: 1200px; height: 900px;
    display: flex; align-items: center; justify-content: center; gap: 60px;
  }
  .card {
    position: relative; width: 525px; height: 300px;
    background: var(--card);
    border: 1px solid var(--card-edge);
    box-shadow: 0 14px 30px rgba(0,0,0,.45);
  }
  /* Front side */
  .card-front { display: flex; }
  .brand-block {
    width: 260px; display: flex; align-items: center; justify-content: center;
    padding-left: 20px;
  }
  .brand-name {
    font-weight: 700; color: var(--brand-green);
    font-size: 36px; line-height: 1.05;
  }
  .divider {
    width: 1px; margin: 40px 0; background: var(--divider);
  }
  .contact-block {
    flex: 1; padding: 50px 0 0 24px; color: var(--ink-light);
    font-size: 13.5px; line-height: 1.35;
  }
  .person-name { color: var(--brand-green); font-weight: 600; font-size: 16px; }
  .person-role { margin-bottom: 18px; }
  .address { margin-bottom: 16px; }
  .contact-line { display: flex; align-items: center; gap: 9px; }
  .contact-line svg { width: 11px; height: 11px; flex: none; }
  /* Back side */
  .card-back { display: flex; align-items: center; justify-content: center; }
  .brand-name-large {
    font-weight: 700; color: var(--silver);
    font-size: 62px; line-height: 1; letter-spacing: 1px;
  }
</style>
</head>
<body>
  <main class="stage">
    <section class="card card-front">
      <div class="brand-block">
        <p class="brand-name">TLK<br>Field Services</p>
      </div>
      <div class="divider"></div>
      <div class="contact-block">
        <p class="person-name">Daniel Hart</p>
        <p class="person-role">Managing Director</p>
        <p class="address">12345, Address Goes Here<br>Country Name, 123456.</p>
        <p class="contact-line">
          <svg viewBox="0 0 12 12" aria-hidden="true"><path d="M2.5 1 L4.5 1 L5.2 3.5 L4 4.5 Q5 7 7.5 8 L8.5 6.8 L11 7.5 L11 9.5 Q10.5 11 9 11 Q1 10 1 3 Q1 1.5 2.5 1 Z" fill="var(--brand-green)"/></svg>
          044-987 654 321
        </p>
        <p class="contact-line">
          <svg viewBox="0 0 12 12" aria-hidden="true"><rect x="1" y="2.5" width="10" height="7" fill="var(--brand-green)"/><path d="M1 2.5 L6 6.5 L11 2.5" stroke="var(--card)" stroke-width="1" fill="none"/></svg>
          info@tlkfield.com
        </p>
        <p class="contact-line">
          <svg viewBox="0 0 12 12" aria-hidden="true"><circle cx="6" cy="6" r="5" fill="var(--brand-green)"/><path d="M1 6 H11 M6 1 Q3 6 6 11 M6 1 Q9 6 6 11" stroke="var(--card)" stroke-width=".8" fill="none"/></svg>
          www.tlkfield.com
        </p>
      </div>
    </section>
    <section class="card card-back">
      <p class="brand-name-large">TLK</p>
    </section>
  </main>
</body>
</html>
```